ALL TEXT Social Media Graphics

We are looking for a series of social media graphics for Instagram (new size: 4:5 (1080 x 1350 pixels) ratio that are ALL TEXT. We want the following quotes below on each graphic; one quote per graphic. AND, In very small letters at the bottom of each graphic, add @PaulaWrenLive
The look and feel of these graphics should be complimentary to the color palette attached below; but keep them simple. But the design is up to you; at the end of this document, I provided various samples of all text graphics that I like as examples.
The Quotes are in the attached WORD document
women trying to lose weight

```html
<!DOCTYPE html>
<html lang="en">
<head>
<meta charset="utf-8">
<title>Sunlit Shape-Up – Social Graphics</title>
<link rel="stylesheet" href="https://fonts.googleapis.com/css2?family=Anton&family=Source+Sans+3:ital,wght@0,400;0,600;0,700;1,700;1,800&display=swap">
<style>
  :root {
    --bg: #e6d6d8;
    --card: #ffffff;
    --pink-light: #fb6cbb;
    --pink: #ef3a7d;
    --berry: #b0004c;
    --ink: #2e2e2e;
  }
  html, body {
    margin: 0;
    width: 1200px;
    height: 1091px;
    overflow: hidden;
    background: var(--bg);
  }
  .board {
    position: relative;
    width: 1200px;
    height: 1091px;
  }
  .card {
    position: absolute;
    width: 270px;
    height: 337px;
    background: var(--card);
    box-sizing: border-box;
    padding: 20px 16px 0 18px;
  }
  .col-1 { left: 24px; }
  .col-2 { left: 317px; }
  .col-3 { left: 611px; }
  .col-4 { left: 904px; }
  .row-1 { top: 20px; }
  .row-2 { top: 374px; }
  .row-3 { top: 730px; }

  .headline {
    margin: 0;
    font-family: "Anton", "Oswald", sans-serif;
    font-weight: 400;
    font-size: 32px;
    line-height: 34.5px;
    letter-spacing: -0.4px;
    color: var(--pink);
    white-space: nowrap;
  }
  .lt { color: var(--pink-light); }
  .md { color: var(--pink); }
  .dk { color: var(--berry); }

  .pitch {
    margin: 26px 0 0;
    max-width: 220px;
    font-family: "Source Sans 3", "Myriad Pro", sans-serif;
    font-size: 18.5px;
    line-height: 23px;
    color: var(--ink);
  }
  .row-2 .pitch, .row-3 .pitch { margin-top: 16px; }
  .pitch--wide { max-width: 236px; }
  .pitch em {
    font-style: italic;
    font-weight: 800;
  }
  .pitch .brand {
    font-style: italic;
    font-weight: 800;
    color: var(--pink);
  }
  .cta {
    position: absolute;
    left: 14px;
    right: 14px;
    text-align: center;
    margin: 0;
    font-family: "Source Sans 3", "Myriad Pro", sans-serif;
    font-size: 14.5px;
    line-height: 18px;
    color: var(--ink);
  }
  .cta strong {
    font-weight: 700;
    color: var(--berry);
  }
  .cta--r1 { top: 270px; }
  .cta--r1b { top: 262px; }
  .cta--r2 { top: 262px; }
  .cta--r3 { top: 254px; }
  .handle {
    position: absolute;
    left: 19px;
    top: 307px;
    margin: 0;
    font-family: "Source Sans 3", "Myriad Pro", sans-serif;
    font-size: 11.5px;
    color: var(--pink);
  }
</style>
</head>
<body>
<main class="board">

  <article class="card col-1 row-1">
    <h2 class="headline"><span class="md">You’ve got</span><br><span class="lt">8 weeks</span> and the<br>perfect plan to<br>drop <span class="dk">30 POUNDS</span></h2>
    <p class="pitch">Let’s <em>get snatched</em> this summer with the <span class="brand">Sunlit Shape-Up.</span></p>
    <p class="cta cta--r1">Comment “<strong>SUMMER</strong>”!</p>
    <p class="handle">@PaulaWrenLive</p>
  </article>

  <article class="card col-2 row-1">
    <h2 class="headline"><span class="lt">Don’t wait ‘til</span><br>next summer<br>to get right<br>The time is <span class="dk">NOW</span></h2>
    <p class="pitch">Drop <em>30 pounds</em> with the <span class="brand">Sunlit Shape-Up.</span></p>
    <p class="cta cta--r1">Comment “<strong>SUMMER</strong>”!</p>
    <p class="handle">@PaulaWrenLive</p>
  </article>

  <article class="card col-3 row-1">
    <h2 class="headline">Sis, we’re <span class="lt">dropping</span><br><span class="lt">belly fat</span> and saying<br>goodbye to<br><span class="dk">STUBBORN POUNDS</span></h2>
    <p class="pitch"><em>Join</em> the <span class="brand">Sunlit Shape-Up</span></p>
    <p class="cta cta--r1">Comment “<strong>SUMMER</strong>”!</p>
    <p class="handle">@PaulaWrenLive</p>
  </article>

  <article class="card col-4 row-1">
    <h2 class="headline">Nothing feels<br>better than seeing<br>that <span class="lt">SCALE DROP</span><br><span class="dk">WEEK AFTER WEEK</span></h2>
    <p class="pitch pitch--wide">Let’s lose up to <em>30 pounds</em> this summer <span class="brand">together.</span></p>
    <p class="cta cta--r1b">Comment “<strong>SUMMER</strong>” to join<br>the Sunlit Shape-Up!</p>
    <p class="handle">@PaulaWrenLive</p>
  </article>

  <article class="card col-1 row-2">
    <h2 class="headline"><span class="lt">SNATCHED WAIST,</span><br>FLAT TUMMY,<br>and<br><span class="dk">30 POUNDS LIGHTER</span></h2>
    <p class="pitch">That’s what the <span class="brand">Sunlit Shape-Up Challenge</span> delivers</p>
    <p class="cta cta--r2">Comment “<strong>SHAPE UP</strong>” to get<br>the plan</p>
    <p class="handle">@PaulaWrenLive</p>
  </article>

  <article class="card col-2 row-2">
    <h2 class="headline"><span class="lt">There’s still time</span><br>to drop the<br><span class="dk">30 POUNDS</span> and<br><span class="lt">slay this summer</span></h2>
    <p class="pitch">The <em>sunlit shape-up</em> has the <span class="brand">blueprint.</span></p>
    <p class="cta cta--r2">Comment “<strong>SHAPE UP</strong>”!</p>
    <p class="handle">@PaulaWrenLive</p>
  </article>

  <article class="card col-3 row-2">
    <h2 class="headline">If your goal<br>is a <span class="lt">TINY WAIST,</span><br>FLAT BELLY, and<br><span class="dk">30 POUNDS DOWN</span></h2>
    <p class="pitch"><em>This</em> is the <span class="brand">Plan.</span></p>
    <p class="cta cta--r2">Comment “<strong>SUMMER</strong>” to join<br>the Sunlit Shape-Up!</p>
    <p class="handle">@PaulaWrenLive</p>
  </article>

  <article class="card col-4 row-2">
    <h2 class="headline"><span class="md">This</span> <span class="lt">summer</span><br>ain’t over and<br>neither are your<br><span class="dk">BODY GOALS</span></h2>
    <p class="pitch pitch--wide">Drop <em>30 pounds</em> with the <span class="brand">Sunlit Shape-Up.</span></p>
    <p class="cta cta--r2">Comment “<strong>SHAPE UP</strong>” to get<br>the plan</p>
    <p class="handle">@PaulaWrenLive</p>
  </article>

  <article class="card col-2 row-3">
    <h2 class="headline">You don’t need<br><span class="lt">another diet</span><br>you need a system<br>that <span class="dk">WORKS</span></h2>
    <p class="pitch pitch--wide">Drop <em>30 pounds</em> with the <span class="brand">Sunlit Shape-Up.</span></p>
    <p class="cta cta--r3">Comment “<strong>SUMMER</strong>” to start now.</p>
    <p class="handle">@PaulaWrenLive</p>
  </article>

  <article class="card col-3 row-3">
    <h2 class="headline">You can <span class="lt">absolutely</span><br>be down<br><span class="dk">20-30 POUNDS</span><br>by end of summer</h2>
    <p class="pitch pitch--wide">All it takes is the <em>right plan</em> and <span class="brand">you’ve found it.</span></p>
    <p class="cta cta--r3">Comment “<strong>SHAPE UP</strong>” for the<br>Sunlit Shape-Up!</p>
    <p class="handle">@PaulaWrenLive</p>
  </article>

</main>
</body>
</html>
```